Post Card Design - Photo on front, details on back. Logo on both sides.

Back: See the photo of my old card. The back worked well, as it gave me lots of space to write on. The address details are still correct, but the logo has changed to Josephine Sans. Logo can be on one line or on two (if two, align it on the left).
Don't include the 'BEAUTIFUL WEDDING DRESSES...' bit.
I'd like to print this on thicker, slightly coarse paper, so don't go too small on detail.
Here are the Plume paper details: Paper Stock: Natural Uncoated
Paper Thickness: Premium
Finish: None
Front of Card: I'd like to see options for both pictures:
I think the painted image would look best with a frame in a pale shade and the logo in the frame fairly subtle.
The actual dress photo I'd like to see cropped a bit like in my mock up. You'll need to have a look at how the logo would be best placed on this. You can place it anywhere, or add a banner.
See my website for my brand's look: mirabeltoft.co.nz
Target Market(s)
Brides
Industry/Entity Type
Wedding Dresses
Contact Information for Business Card
Front: Photo and logo. Back: with details and lots of empty space. See attached photos for loose brief.
Other font styles liked:
- Josephine Sans
Requirements
Must have
- I hand-write the gown designs and price on the back of the card, so there needs to be plenty of empty space.
Nice to have
- As per brief.
Should not have
- It must look clean, romantic, modern. Timeless.

```html
<!DOCTYPE html>
<html lang="en">
<head>
<meta charset="utf-8">
<title>Mira Beltoft – Postcard Set</title>
<link rel="stylesheet" href="https://fonts.googleapis.com/css2?family=Josefin+Sans:wght@200;300;400&display=swap">
<style>
  :root {
    --backdrop: #e8e8e6;
    --stone-light: #efe6d6;
    --stone-mid: #d9c8ab;
    --stone-dark: #a8957a;
    --gown: #f6f3ee;
    --butter: #ecd5a0;
    --bloom-pink: #eea9a4;
    --bloom-cream: #f3ead8;
    --ink-white: #ffffff;
    --ink-dark: #3a3a3c;
    --paper: #f2f2f2;
    --strip: #b9babd;
    --strip-ink: #55565a;
  }
  * { margin: 0; padding: 0; box-sizing: border-box; }
  html, body {
    width: 1200px; height: 720px; overflow: hidden;
    background: var(--backdrop);
    font-family: "Josefin Sans", sans-serif;
  }
  .card {
    position: absolute;
    top: 138px;
    width: 294px; height: 441px;
    overflow: hidden;
    box-shadow: 4px 6px 12px rgba(0,0,0,0.12);
  }
  .card--photo { left: 122px; }
  .card--painting { left: 466px; background: var(--butter); }
  .card--back { left: 811px; top: 134px; height: 440px; background: var(--paper); }

  .photo-fill {
    position: absolute; inset: 0;
    background:
      linear-gradient(100deg, transparent 55%, var(--gown) 78%, var(--gown) 100%),
      linear-gradient(180deg, var(--stone-light) 0%, var(--stone-mid) 55%, var(--stone-dark) 100%);
  }
  .painting-fill {
    position: absolute;
    left: 30px; top: 22px; width: 234px; height: 272px;
    border-radius: 45% 45% 40% 40%;
    background: radial-gradient(ellipse at 55% 45%, var(--bloom-cream) 0%, var(--bloom-pink) 55%, rgba(236,213,160,0) 75%);
  }

  .wordmark {
    position: absolute;
    left: 0; right: 0;
    text-align: center;
    color: var(--ink-white);
    font-weight: 300;
    line-height: 1;
  }
  .wordmark__first { display: block; font-size: 78px; letter-spacing: 5px; font-weight: 200; }
  .wordmark__last { display: block; font-size: 39px; letter-spacing: 1px; margin-top: 8px; font-weight: 200; }
  .card--photo .wordmark { top: 294px; }
  .card--painting .wordmark { top: 302px; }

  .back-name {
    position: absolute;
    left: 40px; bottom: 42px;
    writing-mode: vertical-rl;
    transform: rotate(180deg);
    font-size: 21px; font-weight: 300;
    letter-spacing: 1.5px;
    color: var(--ink-dark);
  }
  .contact-strip {
    position: absolute;
    right: 0; top: 0; bottom: 0;
    width: 46px;
    background: var(--strip);
  }
  .contact-list {
    position: absolute;
    left: 14px; bottom: 40px;
    writing-mode: vertical-rl;
    transform: rotate(180deg);
    list-style: none;
    display: flex; gap: 16px;
    font-size: 11px; font-weight: 400;
    color: var(--strip-ink);
    white-space: nowrap;
  }
  .contact-list li { display: flex; align-items: center; gap: 3px; }
  .contact-list svg { width: 9px; height: 9px; transform: rotate(90deg); }
</style>
</head>
<body>
  <section class="card card--photo">
    <div class="photo-fill" role="img" aria-label="Photograph of a bride in a white fitted gown with a long train, standing in a sunlit stone colonnade"></div>
    <h1 class="wordmark"><span class="wordmark__first">MIRA</span><span class="wordmark__last">BELTOFT</span></h1>
  </section>

  <section class="card card--painting">
    <div class="painting-fill" role="img" aria-label="Vintage painted illustration of an embracing couple surrounded by pink and peach peonies"></div>
    <h1 class="wordmark"><span class="wordmark__first">MIRA</span><span class="wordmark__last">BELTOFT</span></h1>
  </section>

  <section class="card card--back">
    <p class="back-name">MIRA BELTOFT</p>
    <aside class="contact-strip">
      <ul class="contact-list">
        <li>
          <svg viewBox="0 0 10 10" aria-hidden="true"><path d="M2 1l2 2-1 1.2c.6 1.2 1.6 2.2 2.8 2.8L7 6l2 2-1.3 1.3C4.5 9 1 5.5.7 2.3z" fill="currentColor"/></svg>
          +64 9 555 0142
        </li>
        <li>
          <svg viewBox="0 0 10 10" aria-hidden="true"><circle cx="5" cy="5" r="4.2" fill="none" stroke="currentColor" stroke-width="1"/><path d="M1 5h8M5 .8c-2 2.6-2 5.8 0 8.4M5 .8c2 2.6 2 5.8 0 8.4" fill="none" stroke="currentColor" stroke-width=".8"/></svg>
          mirabeltoft.co.nz
        </li>
        <li>
          <svg viewBox="0 0 10 10" aria-hidden="true"><rect x=".7" y="2" width="8.6" height="6" fill="none" stroke="currentColor" stroke-width="1"/><path d="M.7 2L5 5.5 9.3 2" fill="none" stroke="currentColor" stroke-width="1"/></svg>
          mira@mirabeltoft.co.nz
        </li>
      </ul>
    </aside>
  </section>
</body>
</html>
```